Redesign of page from emergency manual

Please redesign this PDF to look better. Please don't include any stock photos. It must be legible. Making some words bold is probably a good idea.

Here are some things I like :

https://tarrowbooks.com.au/collections/frontpage/products/the-plk-v2-ebook

https://img-cd.vostramediafiles.com/qa-ejkwPLOTYY_SuCKbZNu411Qwgjv8YssPxEdzXN93hDkSRjLXK8WmfgbmrJW4ZZ3yUPK=w1052-h592-rw

```html
<!DOCTYPE html>
<html lang="en">
<head>
<meta charset="utf-8">
<title>Hypertension, Acute</title>
<link rel="stylesheet" href="https://fonts.googleapis.com/css2?family=Inter+Tight:ital,wght@0,400;0,500;0,700;0,800;1,700;1,800&display=swap">
<style>
  :root {
    --mint: #90fef0;
    --mint-mid: #a8fcf1;
    --mint-pale: #ebfffc;
    --ink: #0a0a0a;
    --white: #ffffff;
    --rule: #1a1a1a;
    --cream-edge: #f6fbe6;
  }
  * { margin: 0; padding: 0; box-sizing: border-box; }
  html, body { width: 1200px; height: 927px; overflow: hidden; background: var(--white); }
  body { font-family: "Inter Tight", Arial, sans-serif; color: var(--ink); position: relative; }

  .header-band {
    position: absolute; left: 0; top: 0; width: 1102px; height: 193px;
    background: var(--mint); border-bottom-left-radius: 110px;
  }
  .side-tab {
    position: absolute; left: 1110px; top: 0; width: 90px; height: 927px;
    background: var(--mint); border-top-right-radius: 93px;
  }
  .side-title {
    position: absolute; left: 1154px; top: 214px;
    transform-origin: 0 0; transform: rotate(90deg) translateY(-50%);
    font-weight: 800; font-size: 35px; letter-spacing: 0.5px; white-space: nowrap; line-height: 1;
  }
  .page-number {
    position: absolute; left: 1127px; top: 841px; width: 52px; height: 52px; border-radius: 50%;
    background: var(--ink); color: var(--white); font-weight: 800; font-size: 23px;
    display: flex; align-items: center; justify-content: center;
  }

  .page-title {
    position: absolute; left: 104px; top: 62px; font-weight: 800; font-size: 54px; letter-spacing: -0.5px; line-height: 1;
  }
  .title-rule { position: absolute; left: 85px; top: 137px; width: 614px; height: 3px; background: var(--white); }
  .revision { position: absolute; left: 105px; top: 157px; font-size: 13px; color: var(--white); letter-spacing: 0.2px; }

  .definition {
    position: absolute; left: 698px; top: 78px; width: 386px; height: 93px;
    background: var(--mint-pale); border: 2px solid var(--cream-edge); border-radius: 16px;
    display: flex; align-items: center; justify-content: center; text-align: center;
    font-weight: 800; font-style: italic; font-size: 19px; line-height: 23px;
  }

  .intro {
    position: absolute; left: 85px; top: 214px; width: 599px; height: 183px;
    border: 1px solid var(--rule); border-radius: 22px 22px 0 0; overflow: hidden;
  }
  .intro-lead { height: 63px; padding: 10px 20px 0; font-size: 16.5px; line-height: 23px; }
  .intro-lead em { font-weight: 700; }
  .intro-checks { display: flex; height: 119px; background: var(--mint-pale); }
  .check { padding: 16px 20px 0; font-size: 16.5px; line-height: 23px; }
  .check:first-child { width: 301px; }
  .check:last-child { background: var(--mint-pale); border-left: 1px solid #d7f7f2; }
  .check h3 { font-size: 16.5px; font-weight: 800; margin-bottom: 2px; }
  .bullet { display: flex; gap: 8px; }
  .bullet::before { content: "▸"; font-size: 11px; line-height: 23px; }

  .bp-table {
    position: absolute; left: 698px; top: 214px; width: 386px; height: 183px;
    border: 1px solid var(--rule); border-radius: 22px 22px 0 0; overflow: hidden;
  }
  .bp-table h2 {
    height: 45px; background: var(--mint-mid); border-bottom: 1px solid var(--rule);
    font-size: 19.5px; font-weight: 800; text-align: center; line-height: 45px; letter-spacing: -0.2px;
  }
  .bp-table table { width: 100%; border-collapse: collapse; }
  .bp-table td, .bp-table th { width: 33.33%; text-align: center; font-size: 17px; height: 34px; border: 1px solid var(--rule); }
  .bp-table th { font-weight: 800; }
  .bp-table td { font-weight: 400; letter-spacing: 1px; }
  .bp-table tr > :first-child { border-left: 0; }
  .bp-table tr > :last-child { border-right: 0; }
  .bp-table tr:first-child > * { border-top: 0; }
  .bp-table tr:last-child > * { border-bottom: 0; }

  .caution {
    position: absolute; left: 85px; top: 404px; width: 1004px; height: 94px;
    border: 3.5px solid var(--ink); padding: 11px 0 0 17px; display: flex;
  }
  .caution-label { width: 129px; font-weight: 800; font-size: 19px; line-height: 22px; }
  .caution-text { font-size: 16.5px; line-height: 23px; }
  .caution-text strong { font-weight: 800; font-style: italic; }

  .drug-table {
    position: absolute; left: 85px; top: 504px; width: 999px; border-collapse: collapse;
    font-size: 17px; border: 1px solid var(--rule);
  }
  .drug-table th {
    background: var(--mint-mid); height: 45px; text-align: left; font-weight: 800; font-size: 19.5px;
    border-bottom: 2px solid var(--rule);
  }
  .drug-table td { padding-left: 17px; height: 32px; }
  .drug-table .action { width: 301px; background: var(--white); border: 1px solid var(--rule); padding-left: 20px; }
  .drug-table th.action { background: var(--mint-mid); }
  .drug-table .drug { width: 262px; border-left: 1px solid var(--rule); }
  .drug-table .dose b { font-weight: 700; }
  .drug-table tr.strong td:not(.action) { background: var(--mint-mid); }
  .drug-table tr.soft td:not(.action) { background: var(--mint-pale); }
  .drug-table tr.tall td { height: 52px; vertical-align: top; padding-top: 5px; line-height: 24px; }
  .drug-table tr.group-end td { border-bottom: 1px solid var(--rule); }
  .drug-table th.dose { padding-left: 0; }

  .differential {
    position: absolute; left: 85px; top: 801px; width: 999px; height: 104px;
    background: var(--mint-pale); border: 1px solid var(--rule); border-radius: 22px;
    padding: 9px 0 0 20px; display: flex; font-size: 17px; line-height: 20px;
  }
  .differential h2 { width: 283px; font-size: 19.5px; font-weight: 800; line-height: 27px; }
  .differential ul { list-style: none; width: 245px; }
  .differential li { display: flex; gap: 9px; margin-bottom: 3px; }
  .differential li::before { content: "▸"; font-size: 11px; }
</style>
</head>
<body>
  <div class="header-band"></div>
  <div class="side-tab"></div>
  <div class="side-title">HYPERTENSION, ACUTE</div>
  <div class="page-number">12</div>

  <h1 class="page-title">Hypertension, Acute</h1>
  <div class="title-rule"></div>
  <p class="revision">REVISION&nbsp; ▸ &nbsp;Feb 2020</p>

  <p class="definition">Sustained high blood pressure<br>refractory to treating<br>reversible causes</p>

  <section class="intro">
    <p class="intro-lead">In pediatrics, hypertension is almost always treated by addressing likely causes such as <em>light anesthesia</em> or <em>measurement error:</em></p>
    <div class="intro-checks">
      <div class="check">
        <h3>Ensure correct BP cuff size:</h3>
        <p>cuff bladder width ~ 40%<br>of limb circumference</p>
      </div>
      <div class="check">
        <h3>Ensure arterial line transducer<br>is at level of heart</h3>
        <p class="bullet"><span>Consider placing arterial line<br>if not already present</span></p>
      </div>
    </div>
  </section>

  <section class="bp-table">
    <h2>Hypertensive Blood Pressure Range*</h2>
    <table>
      <tr><th>Age (yr)</th><th>Systolic</th><th>Diastolic</th></tr>
      <tr><td>newborn</td><td>&gt;97</td><td>&gt;70</td></tr>
      <tr><td>1-3</td><td>&gt;105</td><td>&gt;61</td></tr>
      <tr><td>4-12</td><td>&gt;113</td><td>&gt;86</td></tr>
    </table>
  </section>

  <section class="caution">
    <p class="caution-label">*CAUTION:</p>
    <p class="caution-text">Anti-hypertensive drugs are almost never needed for routine pediatric cases. These medications are<br>used almost exclusively for specialized cardiac, neurosurgical, or endocrine (pheochromocytoma) cases.<br><strong>Consult an expert before use. Rule-out increased ICP.</strong></p>
  </section>

  <table class="drug-table">
    <tr><th class="action">ACTION</th><th class="drug" style="padding-left:17px">Drug</th><th class="dose">(IV Dosing)</th></tr>
    <tr class="strong"><td class="action" rowspan="2">Direct smooth muscle relaxation</td><td class="drug">Sodium nitroprusside</td><td class="dose"><b>0.5 - 10</b> MICROgrams/kg/min</td></tr>
    <tr class="soft group-end"><td class="drug">HydrALAZINE</td><td class="dose"><b>0.1 - 0.2</b> mg/kg (adult dose 5-10 mg)</td></tr>
    <tr class="strong tall"><td class="action" rowspan="2" style="vertical-align:middle;padding-top:0">β-Adrenergic blockade</td><td class="drug">Esmolol</td><td class="dose"><b>100 - 500</b> MICROgrams/kg over 5 min, then<br><b>25 - 300</b> MICROgrams/kg/min</td></tr>
    <tr class="soft group-end"><td class="drug">Labetalol (also a effect)</td><td class="dose"><b>0.2 - 1</b> mg/kg q 10 min;&nbsp;&nbsp; <b>0.4 - 3</b> mg/kg/hour (infusion)</td></tr>
    <tr class="strong"><td class="action" rowspan="2">Calcium channel blockade</td><td class="drug">niCARdapine</td><td class="dose"><b>0.5 - 5</b> MICROgrams/kg/min</td></tr>
    <tr class="soft group-end"><td class="drug">Clevidipine</td><td class="dose"><b>0.5 - 3.5</b> MICROgrams/kg/min</td></tr>
    <tr class="strong"><td class="action">Direct smooth muscle relaxation</td><td class="drug">Fenoldopam</td><td class="dose"><b>0.2 - 0.8</b> MICROgrams/kg/min</td></tr>
  </table>

  <section class="differential">
    <h2>Consider Differential<br>(Partial):</h2>
    <ul>
      <li><span>Light anesthesia (consider vaporizer <i>or</i> infusion pump empty <i>or</i> malfunctioning)</span></li>
      <li><span>Hypercarbia</span></li>
    </ul>
    <ul>
      <li><span>Hypoxemia</span></li>
      <li><span>Arterial line transducer too low or BP cuff too small</span></li>
      <li><span>Withdrawal (EtOH or opioid)</span></li>
    </ul>
    <ul>
      <li><span>Thyroid Storm</span></li>
      <li><span>Pheochromocytoma</span></li>
      <li><span>Drug Error</span></li>
    </ul>
  </section>
</body>
</html>
```